CoralPeak Travel

We are new traveling company from Italy and looking for a really unique design as soon as possible of the main page.
Travel is an online business. We all do online research before taking a vacation. Since some of us will spend hours researching a trip before finally booking it on a travel website, design is critical.
People looking to travel are going to start with an idea. Some may be browsing for a specific type of trip (river cruise, kayaking, etc.) while others may be looking at specific dates (i.e. February). Still others are considering going to a specific destination such as the Grand Canyon, but all of these visitors are goal-oriented. This type of visitor is frustrated by not finding thle right information easily. This is why travel web design must offer several ways to navigate such as by date, location, activity, cost, etc.
The design should be easy to use for visitors, look fantastic and be easy to update and maintain.
Uploaded some sample pictures but feel free to use your own if it looks good. About colors, blue and white would mix great.

Our future address will be coralpeaktravel.com

```html
<!DOCTYPE html>
<html lang="en">
<head>
<meta charset="utf-8">
<title>CoralPeak Travel</title>
<link rel="stylesheet" href="https://fonts.googleapis.com/css2?family=Open+Sans:wght@400;600;700&family=Arimo:wght@400&display=swap">
<style>
:root{
  --blue:#1e6fb3;
  --blue-dark:#1b5c96;
  --sky:#3fb5e8;
  --sky-dark:#2a6fa6;
  --orange:#f1a01c;
  --text:#555;
  --muted:#888;
  --line:#dedede;
  --footer:#f3f3f3;
  --white:#fff;
  --star:#f5b301;
}
*{box-sizing:border-box;margin:0;padding:0}
html,body{width:1200px;height:2376px;overflow:hidden;background:var(--white)}
body{position:relative;font-family:"Open Sans",sans-serif;color:var(--text)}
.abs{position:absolute}

/* header */
.brand{left:87px;top:54px;font-family:"Open Sans",sans-serif;font-weight:600;font-size:34px;color:var(--blue);letter-spacing:0}
.nav a{position:absolute;top:62px;height:36px;line-height:36px;font-size:17px;color:#666;text-decoration:none;text-transform:uppercase}
.nav .active{left:583px;width:85px;background:var(--sky);color:var(--white);text-align:center}

/* hero */
.hero{left:0;top:139px;width:1200px;height:491px;background:linear-gradient(100deg,#e86a1c 0%,#c9703a 25%,#8d6a5e 50%,#6f8d96 72%,#9fd3e0 100%)}
.hero-title{left:90px;top:320px;font-size:35px;font-weight:700;color:var(--white);text-transform:uppercase;letter-spacing:-.5px}
.dots{left:1032px;top:504px;display:flex;gap:6px}
.dots span{width:16px;height:16px;border-radius:50%;background:rgba(255,255,255,.75)}
.dots span:first-child{background:var(--white)}

/* search */
.search{left:87px;top:579px;width:1026px;height:290px;background:var(--white);box-shadow:0 2px 8px rgba(0,0,0,.25)}
.col{position:absolute;top:20px}
.col h3{font-size:29px;font-weight:700;color:var(--blue-dark);margin-bottom:22px}
.col h3 b{color:var(--orange)}
.label{font-size:16px;color:var(--muted);margin-bottom:10px}
.field{width:168px;height:42px;border:1px solid #ccc;font-size:15px;color:#777;line-height:40px;padding-left:12px;position:relative;margin-bottom:32px}
.field.wide{width:182px}
.field svg{position:absolute;right:10px;top:11px}
.radio{display:flex;align-items:center;gap:12px;font-size:16px;color:#666;height:34px}
.radio i{width:14px;height:14px;border:1px solid #bbb;border-radius:50%;display:inline-block}
.radio i.on{background:radial-gradient(circle,#aaa 30%,transparent 35%)}
.send{left:514px;top:852px;height:35px;display:flex}
.btn-text{background:var(--sky);color:var(--white);font-size:14px;font-weight:700;line-height:35px;text-transform:uppercase}
.btn-arrow{width:32px;background:var(--sky-dark);display:flex;align-items:center;justify-content:center}

/* section titles */
.section-title{font-size:27px;color:var(--blue-dark);font-weight:400;text-transform:uppercase;letter-spacing:.3px}

.slider-arrows{left:1032px;top:947px;display:flex;gap:4px}
.slider-arrows span{width:38px;height:40px;border:1px solid #ddd;display:flex;align-items:center;justify-content:center}

/* category cards */
.card{position:absolute;top:1019px;width:304px}
.card .photo{height:208px}
.card h4{margin-top:25px;font-size:19px;font-weight:600;color:var(--blue-dark);text-transform:uppercase}
.card p{margin-top:12px;font-size:14.5px;line-height:29px;color:#777}
.card .book{margin-top:16px;display:flex;height:36px}
.card .book .btn-text{width:149px;text-align:center;line-height:36px}

/* hot deals */
.deal{position:absolute;left:90px;width:640px}
.deal .photo{position:absolute;left:0;top:0;width:209px;height:154px;border:5px solid var(--white);box-shadow:0 1px 5px rgba(0,0,0,.3)}
.deal h5{position:absolute;left:238px;top:4px;font-family:"Arimo",sans-serif;font-size:21px;font-weight:400;color:#222;white-space:nowrap}
.deal p{position:absolute;left:238px;top:42px;width:402px;font-size:14.5px;line-height:26px;color:#666}
.deal .stars{position:absolute;left:238px;top:128px;display:flex;gap:4px}

.cat-list{left:809px;top:1532px;width:304px;list-style:none}
.cat-list li{height:44.6px;border-bottom:1px solid var(--line);font-size:15.5px;color:#666;display:flex;align-items:center;gap:12px;padding-left:4px}
.cat-list li:nth-child(5){border-bottom:2px solid #ccc}

/* footer */
.footer{left:0;top:1964px;width:1200px;height:317px;background:var(--footer)}
.footer p.about{position:absolute;left:87px;top:92px;width:372px;font-size:14.5px;line-height:28px;color:#555}
.news{position:absolute;left:512px;width:300px}
.news .thumb{position:absolute;left:0;top:0;width:68px;height:64px}
.news .n-title{position:absolute;left:85px;top:-2px;font-size:15px;color:var(--blue)}
.news .n-text{position:absolute;left:85px;top:20px;width:170px;font-size:14px;line-height:26px;color:#666}
.contact-addr{left:829px;top:2065px;font-size:17px;color:#555}
.contact-phone{left:829px;top:2098px;font-size:22px;color:var(--sky)}
.social{left:832px;top:2150px;display:flex;gap:26px}
.social span{width:38px;height:38px;border-radius:50%}
.bottom{left:0;top:2281px;width:1200px;height:95px;background:var(--white)}
.bottom span{position:absolute;top:34px;font-family:"Arimo",sans-serif;font-size:16px;color:#333}
</style>
</head>
<body>

<header>
  <div class="abs brand">CoralPeak Travel</div>
  <nav class="nav">
    <a class="active" href="#">Home</a>
    <a href="#" style="left:697px">Activities</a>
    <a href="#" style="left:824px">Tours</a>
    <a href="#" style="left:921px">Hotels</a>
    <a href="#" style="left:1026px">Contacts</a>
  </nav>
</header>

<section class="abs hero" role="img" aria-label="Large seashell on a sandy beach at sunset with the sea washing in"></section>
<h1 class="abs hero-title">The destination of your dreams</h1>
<div class="abs dots"><span></span><span></span><span></span><span></span></div>

<form class="abs search">
  <div class="col" style="left:27px">
    <h3><b>01.</b>Date</h3>
    <div class="label">Check-in date</div>
    <div class="field">20/05/2014
      <svg width="20" height="18" viewBox="0 0 20 18"><rect x="1" y="2" width="18" height="15" fill="none" stroke="#aaa"/><path d="M1 6h18M5 9h2M9 9h2M13 9h2M5 12h2M9 12h2M13 12h2" stroke="#aaa"/></svg>
    </div>
    <div class="label">Check-in date</div>
    <div class="field">20/05/2014
      <svg width="20" height="18" viewBox="0 0 20 18"><rect x="1" y="2" width="18" height="15" fill="none" stroke="#aaa"/><path d="M1 6h18M5 9h2M9 9h2M13 9h2M5 12h2M9 12h2M13 12h2" stroke="#aaa"/></svg>
    </div>
  </div>
  <div class="col" style="left:279px">
    <h3><b>02.</b>Location</h3>
    <div class="label">Destination</div>
    <div class="field wide"></div>
    <div class="label">Your e-mail</div>
    <div class="field wide"></div>
  </div>
  <div class="col" style="left:552px">
    <h3><b>03.</b>Activity</h3>
    <div class="radio"><i class="on"></i>River Cruise</div>
    <div class="radio"><i></i>kayaking</div>
    <div class="radio"><i></i>Trekking</div>
    <div class="radio"><i></i>Cycling</div>
    <div class="radio"><i></i>Boating</div>
  </div>
  <div class="col" style="left:818px">
    <h3><b>02.</b>Cost</h3>
    <div class="label">Minimum</div>
    <div class="field wide">$ 104
      <svg width="14" height="16" viewBox="0 0 14 16"><path d="M2 6l5 5 5-5z" fill="#777"/></svg>
    </div>
    <div class="label">Maximum</div>
    <div class="field wide">$ 2456K
      <svg width="14" height="16" viewBox="0 0 14 16"><path d="M2 6l5 5 5-5z" fill="#777"/></svg>
    </div>
  </div>
</form>
<div class="abs send">
  <span class="btn-text" style="width:147px;text-align:center">Send a request</span>
  <span class="btn-arrow"><svg width="10" height="14" viewBox="0 0 10 14"><path d="M2 1l6 6-6 6" fill="none" stroke="#fff" stroke-width="2.5"/></svg></span>
</div>

<h2 class="abs section-title" style="left:89px;top:948px">Travel categories</h2>
<div class="abs slider-arrows">
  <span><svg width="10" height="14" viewBox="0 0 10 14"><path d="M8 1L2 7l6 6" fill="none" stroke="#2a6fa6" stroke-width="2"/></svg></span>
  <span><svg width="10" height="14" viewBox="0 0 10 14"><path d="M2 1l6 6-6 6" fill="none" stroke="#2a6fa6" stroke-width="2"/></svg></span>
</div>

<article class="card" style="left:87px">
  <div class="photo" role="img" aria-label="Passenger airliner flying through a blue sky with clouds" style="background:linear-gradient(180deg,#4a76b8,#9bb9df 70%,#c6d7ea)"></div>
  <h4>Airline tickets</h4>
  <p>Lorem ipsum dolor sit amet consectetuer adi piscing elit Nam cursus Morbi ut mi. Nullam</p>
  <div class="book"><span class="btn-text">Book now</span><span class="btn-arrow"><svg width="10" height="14" viewBox="0 0 10 14"><path d="M2 1l6 6-6 6" fill="none" stroke="#fff" stroke-width="2.5"/></svg></span></div>
</article>
<article class="card" style="left:451px">
  <div class="photo" role="img" aria-label="Hotel terrace with armchairs beside a pool at dusk" style="background:linear-gradient(180deg,#c8905c,#7a5a44 50%,#3f8fa8)"></div>
  <h4>Hotels</h4>
  <p>Lorem ipsum dolor sit amet consectetuer adi piscing elit Nam cursus Morbi ut mi. Nullam</p>
  <div class="book"><span class="btn-text">Book now</span><span class="btn-arrow"><svg width="10" height="14" viewBox="0 0 10 14"><path d="M2 1l6 6-6 6" fill="none" stroke="#fff" stroke-width="2.5"/></svg></span></div>
</article>
<article class="card" style="left:811px">
  <div class="photo" role="img" aria-label="White cruise ship sailing on turquoise sea" style="background:linear-gradient(180deg,#2a8fd0,#4ab6e0 45%,#1ea3b8)"></div>
  <h4>Cruises</h4>
  <p>Lorem ipsum dolor sit amet consectetuer adi piscing elit Nam cursus Morbi ut mi. Nullam</p>
  <div class="book"><span class="btn-text">Book now</span><span class="btn-arrow"><svg width="10" height="14" viewBox="0 0 10 14"><path d="M2 1l6 6-6 6" fill="none" stroke="#fff" stroke-width="2.5"/></svg></span></div>
</article>

<h2 class="abs section-title" style="left:87px;top:1476px">Hot deals</h2>
<h2 class="abs section-title" style="left:809px;top:1476px">Categories</h2>

<article class="deal" style="top:1542px">
  <div class="photo" role="img" aria-label="Warm-lit hotel room with a bed" style="background:linear-gradient(135deg,#8a5a34,#c98c52 50%,#6b4630)"></div>
  <h5>Quisque sagittis semper felis condimt</h5>
  <p>Duis autem vel eum iriure &nbsp;dolor in hendreritvulputate velit esse molestie consequat, vnllum dolore eu feugiat nulla fac ilisis at vero eros accumsan et iusto odio dignissim.</p>
  <div class="stars">
    <svg width="108" height="18" viewBox="0 0 108 18"><g stroke="#f5b301" stroke-width="1.2"><path d="M9 1l2.4 5 5.4.6-4 3.7 1.1 5.4L9 13l-4.9 2.7 1.1-5.4-4-3.7 5.4-.6z" fill="#f5b301"/><path transform="translate(22 0)" d="M9 1l2.4 5 5.4.6-4 3.7 1.1 5.4L9 13l-4.9 2.7 1.1-5.4-4-3.7 5.4-.6z" fill="none"/><path transform="translate(44 0)" d="M9 1l2.4 5 5.4.6-4 3.7 1.1 5.4L9 13l-4.9 2.7 1.1-5.4-4-3.7 5.4-.6z" fill="none"/><path transform="translate(66 0)" d="M9 1l2.4 5 5.4.6-4 3.7 1.1 5.4L9 13l-4.9 2.7 1.1-5.4-4-3.7 5.4-.6z" fill="none"/><path transform="translate(88 0)" d="M9 1l2.4 5 5.4.6-4 3.7 1.1 5.4L9 13l-4.9 2.7 1.1-5.4-4-3.7 5.4-.6z" fill="none"/></g></svg>
  </div>
</article>
<article class="deal" style="top:1734px">
  <div class="photo" role="img" aria-label="Overwater villas lit at dusk below mountains" style="background:linear-gradient(180deg,#2d5fa8,#6a8fc4 45%,#23466e)"></div>
  <h5>Quisque sagittis semper felis condimt</h5>
  <p>Duis autem vel eum iriure &nbsp;dolor in hendreritvulputate velit esse molestie consequat, vnllum dolore eu feugiat nulla fac ilisis at vero eros accumsan et iusto odio dignissim.</p>
  <div class="stars">
    <svg width="108" height="18" viewBox="0 0 108 18"><g stroke="#f5b301" stroke-width="1.2"><path d="M9 1l2.4 5 5.4.6-4 3.7 1.1 5.4L9 13l-4.9 2.7 1.1-5.4-4-3.7 5.4-.6z" fill="#f5b301"/><path transform="translate(22 0)" d="M9 1l2.4 5 5.4.6-4 3.7 1.1 5.4L9 13l-4.9 2.7 1.1-5.4-4-3.7 5.4-.6z" fill="none"/><path transform="translate(44 0)" d="M9 1l2.4 5 5.4.6-4 3.7 1.1 5.4L9 13l-4.9 2.7 1.1-5.4-4-3.7 5.4-.6z" fill="none"/><path transform="translate(66 0)" d="M9 1l2.4 5 5.4.6-4 3.7 1.1 5.4L9 13l-4.9 2.7 1.1-5.4-4-3.7 5.4-.6z" fill="none"/><path transform="translate(88 0)" d="M9 1l2.4 5 5.4.6-4 3.7 1.1 5.4L9 13l-4.9 2.7 1.1-5.4-4-3.7 5.4-.6z" fill="none"/></g></svg>
  </div>
</article>

<ul class="abs cat-list">
  <li><svg width="7" height="11" viewBox="0 0 7 11"><path d="M1 1l4.5 4.5L1 10" fill="none" stroke="#888" stroke-width="1.5"/></svg>Phasellus felis dolor scelerisque</li>
  <li><svg width="7" height="11" viewBox="0 0 7 11"><path d="M1 1l4.5 4.5L1 10" fill="none" stroke="#888" stroke-width="1.5"/></svg>Tempus eget lobortis id libero.</li>
  <li><svg width="7" height="11" viewBox="0 0 7 11"><path d="M1 1l4.5 4.5L1 10" fill="none" stroke="#888" stroke-width="1.5"/></svg>Aliquam nec erat at purus cursus</li>
  <li><svg width="7" height="11" viewBox="0 0 7 11"><path d="M1 1l4.5 4.5L1 10" fill="none" stroke="#888" stroke-width="1.5"/></svg>Vestibulum ligula augue</li>
  <li><svg width="7" height="11" viewBox="0 0 7 11"><path d="M1 1l4.5 4.5L1 10" fill="none" stroke="#888" stroke-width="1.5"/></svg>Bibendum accumsan vestibulum</li>
  <li><svg width="7" height="11" viewBox="0 0 7 11"><path d="M1 1l4.5 4.5L1 10" fill="none" stroke="#888" stroke-width="1.5"/></svg>Phasellus felis dolor scelerisque</li>
  <li><svg width="7" height="11" viewBox="0 0 7 11"><path d="M1 1l4.5 4.5L1 10" fill="none" stroke="#888" stroke-width="1.5"/></svg>Tempus eget lobortis id libero.</li>
  <li><svg width="7" height="11" viewBox="0 0 7 11"><path d="M1 1l4.5 4.5L1 10" fill="none" stroke="#888" stroke-width="1.5"/></svg>Aliquam nec erat at purus cursus</li>
</ul>

<footer class="abs footer">
  <h2 class="abs section-title" style="left:87px;top:40px">About</h2>
  <p class="about">Aenean nonummy hendrerit mauris. Phasellus porta. Fusce suscipit varius mi. Cum sociis natoque penatibus et magnis dis parturient montes, nascetur ridiculus mus. Nulla dui. Fusce feugiat malesuada odio. Morbi nunc odio, gravidaat. Nulla dui. Fusce feugiat malesuada odio. Morbi nunc odio, gravida at, cursus nec. Duis ultricies pharetra magna.</p>

  <h2 class="abs section-title" style="left:512px;top:40px">Travel news</h2>
  <div class="news" style="top:102px">
    <div class="thumb" role="img" aria-label="Traveller in a sun hat by the sea" style="background:linear-gradient(135deg,#e8c07a,#5ab6d8)"></div>
    <div class="n-title">Phasellus porta.</div>
    <div class="n-text">Fusce suscipit varius mi. Cum sociis noque pen</div>
  </div>
  <div class="news" style="top:190px">
    <div class="thumb" role="img" aria-label="Seaside resort buildings under a blue sky" style="background:linear-gradient(180deg,#6fa6d6,#c9a27a)"></div>
    <div class="n-title">Phasellus porta.</div>
    <div class="n-text">Fusce suscipit varius mi. Cum sociis noque pen</div>
  </div>

  <h2 class="abs section-title" style="left:829px;top:40px">Follow us</h2>
</footer>
<div class="abs contact-addr">412 Harbour Lane, Portmere, K17.</div>
<div class="abs contact-phone">+1 800 555 0142</div>
<div class="abs social" aria-label="Social profiles">
  <span style="background:#3b5b9a"></span>
  <span style="background:#333"></span>
  <span style="background:#2ca7e0"></span>
  <span style="background:#1b82c2"></span>
</div>

<div class="abs bottom">
  <span style="left:89px">Terms and Conditions | Privacy Policy | FAQ's</span>
  <span style="right:87px">Copyright © 2014. All Rights Reserved.</span>
</div>

</body>
</html>
```